Brochure for Flooring

Brochure for bamboo flooring company.

Size can be any size, we aren't married to specific dimension / type.

Files for logo, text, and some photos to get started attached. Designer can also use placeholder photos that we can switch out later.

Themes are Eco Friendly, natural, bamboo...

Thanks, and look forward to seeing your design.

Industry/Entity Type

Flooring

```html
<!DOCTYPE html>
<html lang="en">
<head>
<meta charset="utf-8">
<title>Bamboo Flooring Brochure</title>
<link href="https://fonts.googleapis.com/css2?family=Arimo:wght@400;700&display=swap" rel="stylesheet">
<style>
:root{
  --backdrop:#d9d6d0;
  --page-tan:#9a8354;
  --photo-dark:#4a2e1c;
  --photo-mid:#8a6a44;
  --photo-light:#d8c8a8;
  --band-brown:#6b4a2c;
  --card-white:#ffffff;
  --card-cream:#f4efe2;
  --title-brown:#7a5a34;
  --leaf-green:#8dc63f;
  --text-white:#ffffff;
  --text-brown:#7a5a34;
  --overlay:rgba(60,40,22,.72);
}
*{margin:0;padding:0;box-sizing:border-box}
html,body{width:1200px;height:900px;overflow:hidden}
body{background:var(--backdrop);font-family:"Arimo",Arial,sans-serif;position:relative}
.spread{position:absolute;left:20px;top:116px;width:1160px;height:634px;box-shadow:0 6px 18px rgba(0,0,0,.25)}
.page-left{position:absolute;left:0;top:0;width:576px;height:634px;background:var(--band-brown)}
.room-photo{position:absolute;left:0;top:0;width:576px;height:564px;
  background:linear-gradient(160deg,var(--photo-light) 0%,var(--photo-mid) 45%,var(--photo-dark) 80%)}
.intro-card{position:absolute;left:256px;top:4px;width:236px;height:310px;background:var(--card-white);border-top-right-radius:22px}
.intro-title{position:absolute;left:18px;top:68px;font-weight:700;font-size:19px;line-height:22px;color:var(--title-brown);letter-spacing:.5px}
.intro-title .green{color:var(--leaf-green)}
.intro-body{position:absolute;left:14px;top:134px;width:190px;padding:6px;background:var(--card-cream);font-weight:700;font-size:9.5px;line-height:14px;color:var(--text-brown)}
.eco-box{position:absolute;left:30px;top:414px;width:500px;height:120px;background:var(--overlay);padding:8px 12px}
.eco-box h3{font-size:14px;color:var(--leaf-green);margin-bottom:4px}
.eco-box h3 span{color:var(--text-white)}
.eco-box p{font-weight:700;font-size:9.5px;line-height:13.5px;color:var(--text-white)}
.page-right{position:absolute;left:576px;top:0;width:584px;height:634px;background:var(--page-tan)}
.section{position:absolute}
.section h3{font-size:14px;color:var(--leaf-green);margin-bottom:6px;letter-spacing:.5px}
.section p{font-weight:700;font-size:9.5px;line-height:14px;color:var(--text-white)}
</style>
</head>
<body>
<div class="spread">
  <div class="page-left">
    <div class="room-photo" role="img" aria-label="Living room with leather sofa on a warm bamboo floor"></div>
    <div class="intro-card">
      <h1 class="intro-title">BAMBOO FLOORING<br>FOR <span class="green">GREEN</span> LIVING</h1>
      <p class="intro-body">Enjoy the exotic appearance and eco-friendly durability of Sylvara Bamboo Floorings. Mature bamboo is carefully selected and manufactured using under ISO9001:2000, CE and Eco Standard quality control systems. Sylvara Bamboo Flooring's are specially manufactured for the demanding Indian Climate</p>
    </div>
    <div class="eco-box">
      <h3>Eco-<span>Friendly</span></h3>
      <p>All Sylvara Bamboo floors are built with the environment in mind. Renewable bamboo from well managed plantations is sourced, with the ecosystem in mind. Manufacturing is done to keep pollutants to a minimum. Emissions on finished product exceed E-1 standards for health and safety, and manufacturing conditions are controlled to limit carbon footprint.</p>
    </div>
  </div>
  <div class="page-right">
    <div class="section" style="left:60px;top:28px;width:222px">
      <h3>Coating</h3>
      <p>To ensure a lifetime of beauty we use a registered 6-layer aluminum-oxide German Technology, using Kellmann Coating. Scratch &amp; Wear Resistant, it provides beautiful protection to your bamboo floor.</p>
    </div>
    <div class="section" style="left:296px;top:28px;width:268px">
      <h3>Bamboo</h3>
      <p>Bamboo is extremely environmentally friendly. Bamboo is a grass, not a wood, so it is a very renewable resource. Poles take 1 year to grow to full size, and 3 - 4 years to achieve maturity. Bamboo stand releases 35%more oxygen than any other tree. Bamboo helps conserve soil and the dense litter of bamboo leaves provide ideal material for compost manure.</p>
    </div>
    <div class="section" style="left:60px;top:142px;width:222px">
      <h3>SNAPLOCK</h3>
      <p>Interior floors are molded with the patented SNAPLOCK profile, which allows for a fast, strong and glue-free installation.</p>
    </div>
    <div class="section" style="left:60px;top:236px;width:504px">
      <h3>Installation</h3>
      <p>Contact a professional installer with experience in solid wood flooring. Floor must be installed over a dry, flat substrate. Ensure that a moisture barrier is put between sub-floor and floor to prevent moisture creeping up. To allow for expansion, make sure there is a gap of 10mm between walls and floor with For complete installation instructions, please contact Greenreach Agro Industries Private Limited or your Local Distributor.</p>
    </div>
    <div class="section" style="left:60px;top:352px;width:504px">
      <h3>Maintenance</h3>
      <p>Proper maintenance your Sylvara Bamboo Floor is essential. Vacuum or sweep regularly. Use a damp mop, avoid pools of water resting on the floor. Use floor mats in all entry and exit ways. Cover sharp ends of tables, chairs and appliances with felt shoes.</p>
    </div>
    <div class="section" style="left:60px;top:446px;width:504px">
      <h3>Warranty</h3>
      <p>Greenreach Agro Industries (P) Ltd, warrants to the original purchaser that it's Sylvara Bamboo Flooring is free from manufacturing defects in material and workmanship at the time of purchase. Greenreach Agro Industries (P) Ltd. gives a lifetime guarantee against delamination to the original purchaser. This warranty does not extend to damage caused by accidents, alterations, misuse, abuse, normal wear and tear, direct exposure to the elements and improper installation which are beyond the manufacturer's control. This warranty does not apply to the exterior finish beyond factory defects since life of the finish will depend on use, care and cleaning.</p>
    </div>
  </div>
</div>
</body>
</html>
```